I need a design for Corvane Homes which is a custom home builder. The name on it will be Dan Hartley, and I will give the phone number to the winning design. No address or website needed.

```html
<!DOCTYPE html>
<html lang="en">
<head>
<meta charset="UTF-8">
<title>Corvane Homes – Dan Hartley</title>
<link rel="stylesheet" href="https://fonts.googleapis.com/css2?family=Noto+Sans:wght@300;400;700&display=swap">
<style>
  :root {
    --brand-blue: #0a9be0;
    --ink: #2f2f33;
    --paper: #ffffff;
    --hill-lime: #d7d224;
    --hill-shadow: #6a6b6b;
    --house-tint: #e1e4f3;
    --house-tint-soft: #f3f4fa;
  }
  * { margin: 0; padding: 0; box-sizing: border-box; }
  html, body {
    width: 1200px;
    height: 627px;
    overflow: hidden;
    background: var(--paper);
  }
  .card {
    position: relative;
    width: 1200px;
    height: 627px;
    background: var(--paper);
    font-family: "Noto Sans", Verdana, sans-serif;
    overflow: hidden;
  }
  .card__scenery {
    position: absolute;
    inset: 0;
  }
  .card__contact {
    position: absolute;
    right: 184px;
    top: 92px;
    text-align: right;
  }
  .card__name {
    font-weight: 700;
    font-size: 44px;
    line-height: 1.1;
    color: var(--brand-blue);
    letter-spacing: -0.5px;
  }
  .card__role {
    font-weight: 400;
    font-size: 26px;
    line-height: 1.3;
    color: var(--ink);
  }
  .card__company {
    position: absolute;
    right: 180px;
    top: 486px;
    font-weight: 300;
    font-size: 66px;
    line-height: 1;
    color: var(--paper);
    white-space: nowrap;
  }
</style>
</head>
<body>
  <div class="card">
    <svg class="card__scenery" width="1200" height="627" viewBox="0 0 1200 627" xmlns="http://www.w3.org/2000/svg">
      <defs>
        <linearGradient id="houses-tone" x1="0" y1="0" x2="0" y2="1">
          <stop offset="0" stop-color="var(--house-tint-soft)"/>
          <stop offset="1" stop-color="var(--house-tint)"/>
        </linearGradient>
      </defs>
      <rect class="houses-illustration" role="img" aria-label="Row of three pale house silhouettes with chimneys along the hillside"
            x="0" y="190" width="1075" height="320" fill="url(#houses-tone)"/>
      <path class="hill-shadow" fill="var(--hill-shadow)"
            d="M24,500 C400,430 800,370 965,369 C1100,370 1190,390 1194,395 L1200,585 L1200,627 L24,627 Z"/>
      <path class="hill" fill="var(--hill-lime)"
            d="M24,502 C400,432 800,382 940,381 C1080,382 1180,410 1196,418 L1194,627 L24,627 Z"/>
    </svg>

    <div class="card__contact">
      <p class="card__name">Dan Hartley</p>
      <p class="card__role">Director</p>
    </div>

    <p class="card__company">Corvane Homes</p>
  </div>
</body>
</html>
```